New look for an established Travel booking site
10 year old design needs a new clean look and better usability
New look for an established Travel booking site - Travel
Creative Brief
Travel
lodgingmeadow.co.uk
We are a uk based web development company with over 10 years of experience. We often use external designers and have run several competitions on another design site, choosing a winner on each occasion.
Like: simple search box high on left hand side, eg http://www.nightquill.com/ navigation layout on http://www.roamfable.com/ (as in 'plan the perfect trip') blue colours in header of http://www.quietbarrow.co.uk/ clear layout in http://herefordshire.bedpeak.co.uk/ Dislikes: clutter too flashy
Service Oriented
#006633 or similar #4D7F3B etc for page background maybe
left side
http://www.roamfable.com/
http://herefordshire.bedpeak.co.uk/
http://nightquill.com
We are certainly NOT looking for a cut and paste job on the above websites! They are listed to give you an idea of the features we want to see on the page, we need to finish up with a page that is clean, attractive, and not confusing to the visitor. There need to be room for the current ads, and the home page will carry a uk map, but about 30% of the size of the current one. Green and blue for basic page colours.. There will be a photo on the homepage... probably an example of a hotel on site - eg http://www.lodgingmeadow.co.uk/places/307.html Existing site: lodgingmeadow.co.uk

```html
<!DOCTYPE html>
<html lang="en">
<head>
<meta charset="utf-8">
<title>Lodging Meadow – over 30,000 places to stay in the UK</title>
<link rel="stylesheet" href="https://fonts.googleapis.com/css2?family=Arimo:wght@400;700&display=swap">
<style>
  :root {
    --green-dark: #2f7a1f;
    --green: #4d9a2a;
    --green-light: #7cc14a;
    --blue-deep: #1f6fc0;
    --blue: #3d95dc;
    --blue-pale: #cfe7f8;
    --link-blue: #1b5fa8;
    --text-grey: #555;
    --white: #fff;
    --field-border: #9ab;
  }
  * { box-sizing: border-box; margin: 0; padding: 0; }
  html, body { width: 1200px; height: 969px; overflow: hidden; background: var(--white); }
  body { font-family: "Arimo", Arial, sans-serif; position: relative; color: #333; }

  /* Header */
  .brand { position: absolute; left: 16px; top: 12px; display: flex; align-items: center; gap: 14px; }
  .brand-mark { width: 58px; height: 58px; background: var(--green); }
  .brand-name { font-size: 34px; font-weight: 700; color: var(--green); line-height: 1; }
  .brand-tagline { font-size: 17px; color: var(--text-grey); margin-top: 6px; }

  .converter { position: absolute; left: 600px; top: 34px; font-size: 17px; }
  .converter-row { display: flex; gap: 8px; margin-top: 4px; }
  .field { height: 26px; border: 1px solid var(--field-border); background: #fff; font-size: 13px; color: #999; padding: 4px 6px; }
  .converter .field { width: 170px; }
  .btn-small { height: 26px; padding: 0 12px; background: var(--green); color: var(--white); font-size: 14px; font-weight: 700; display: flex; align-items: center; border-radius: 3px; }
  .rate { font-size: 12px; margin-top: 6px; }

  .site-search { position: absolute; left: 934px; top: 34px; font-size: 17px; }
  .site-search .field { width: 164px; }
  .advanced { font-size: 12px; color: var(--link-blue); text-decoration: underline; font-weight: 700; margin-top: 6px; display: block; }

  /* Navigation */
  .main-nav { position: absolute; left: 13px; top: 132px; width: 1174px; height: 36px; background: linear-gradient(var(--green-light), var(--green)); border-radius: 6px 6px 0 0; display: flex; align-items: center; padding-left: 6px; }
  .main-nav a { color: var(--white); font-weight: 700; font-size: 17px; text-decoration: none; padding: 0 14px; height: 28px; display: flex; align-items: center; border-right: 1px solid rgba(255,255,255,.5); }
  .main-nav a.active { background: var(--green-dark); border-radius: 4px 4px 0 0; }

  /* Content area */
  .content { position: absolute; left: 13px; top: 170px; width: 1174px; height: 728px; background: linear-gradient(var(--blue-deep) 0%, var(--blue) 45%, #7fbde9 70%, var(--blue-pale) 100%); }
  .panel-title { position: absolute; top: 8px; height: 44px; background: linear-gradient(var(--green-light), var(--green)); color: var(--white); font-weight: 700; font-size: 24px; display: flex; align-items: center; padding: 0 16px; border-radius: 4px; }
  .map-title { left: 8px; width: 384px; }
  .search-title { left: 800px; width: 366px; justify-content: center; }

  .travel-map { position: absolute; left: 10px; top: 60px; width: 770px; height: 380px; background: radial-gradient(ellipse at center, #5aaeea, var(--blue) 70%); border-radius: 6px; }

  .hotel-search { position: absolute; left: 820px; top: 62px; width: 320px; color: var(--white); }
  .hotel-search label { display: block; font-weight: 700; font-size: 22px; margin: 12px 0 6px; }
  .hotel-search .input { height: 34px; background: #fff; border: 1px solid var(--field-border); color: #555; font-size: 17px; padding: 6px 10px; width: 260px; display: flex; justify-content: space-between; align-items: center; }
  .select-arrow { width: 0; height: 0; border-left: 7px solid transparent; border-right: 7px solid transparent; border-top: 9px solid #666; }
  .date-row { display: flex; align-items: center; gap: 8px; }
  .date-row .input { width: 220px; }
  .calendar-icon { width: 26px; height: 24px; background: #fff; border: 2px solid var(--blue-deep); border-top-width: 6px; }
  .search-button { margin: 18px 0 0 98px; width: 102px; height: 36px; background: linear-gradient(var(--green-light), var(--green)); color: var(--white); font-weight: 700; font-size: 19px; display: flex; align-items: center; justify-content: center; border-radius: 4px; }

  .airport-art { position: absolute; left: 848px; top: 430px; width: 190px; height: 160px; background: radial-gradient(circle, #f1d38a, #c8a25a 60%, transparent 72%); }

  .features { position: absolute; left: 76px; top: 480px; color: var(--white); font-size: 15px; line-height: 19px; list-style: none; }
  .features li::before { content: ""; display: inline-block; width: 6px; height: 6px; background: var(--white); margin-right: 8px; vertical-align: middle; }

  .towns { position: absolute; left: 46px; top: 580px; width: 1100px; }
  .towns h2 { color: var(--green-dark); font-size: 20px; margin-bottom: 8px; }
  .towns p { color: var(--link-blue); font-size: 13.5px; line-height: 26px; }

  /* Footer */
  .site-footer { position: absolute; left: 13px; top: 908px; width: 1174px; height: 56px; background: linear-gradient(var(--green-light), var(--green)); display: flex; align-items: center; padding: 0 24px; color: var(--white); font-size: 15px; }
  .site-footer nav { display: flex; gap: 44px; }
  .copyright { margin-left: auto; font-weight: 700; font-size: 13px; }
</style>
</head>
<body>
  <header>
    <div class="brand">
      <div class="brand-mark"></div>
      <div>
        <div class="brand-name">Lodging Meadow</div>
        <div class="brand-tagline">over 30,000 places to stay in the UK</div>
      </div>
    </div>
    <div class="converter">
      <div>Currency Convertor:</div>
      <div class="converter-row">
        <div class="field">Enter an amount here</div>
        <div class="btn-small">Euro</div>
        <div class="btn-small">USD</div>
      </div>
      <div class="rate">Today's Rate: £1 = $ 1.596 or € 1.170</div>
    </div>
    <div class="site-search">
      <div>Search:</div>
      <div class="converter-row">
        <div class="field">Search here</div>
        <div class="btn-small">Search</div>
      </div>
      <a class="advanced">Advanced Search</a>
    </div>
  </header>

  <nav class="main-nav">
    <a class="active">Home</a><a>Holiday Park</a><a>Caravan Park</a><a>Hostels</a><a>Hotels</a><a>Travel Lodges</a><a>Camping</a>
  </nav>

  <main class="content">
    <div class="panel-title map-title">Travel Map 30,000 Places</div>
    <div class="travel-map" role="img" aria-label="World map with clusters of accommodation markers"></div>

    <div class="panel-title search-title">Travel Search Hotels</div>
    <form class="hotel-search">
      <label>Enter your destination</label>
      <div class="input">Hotel, Attraction, Postcode</div>
      <label>Arrival date</label>
      <div class="date-row"><div class="input">Mon 22 Nov 2010 <span class="select-arrow"></span></div><div class="calendar-icon"></div></div>
      <label>No. of nights</label>
      <div class="input">1 Night <span class="select-arrow"></span></div>
      <label>Room Sleeps</label>
      <div class="input">1 Person <span class="select-arrow"></span></div>
      <div class="search-button">Search</div>
    </form>

    <div class="airport-art" role="img" aria-label="Illustration of an airport control tower with a plane taking off"></div>

    <ul class="features">
      <li>We list 13,000 establishments bookable online.</li>
      <li>We feature a further 3000 with direct links</li>
      <li>We include 13,000 more with contact details.</li>
      <li>Lodging Meadow - more places to stay in the UK than any other</li>
    </ul>

    <section class="towns">
      <h2>Towns</h2>
      <p>Aberdeen Hotels | Bath Hotels | Belfast Hotels | Birmingham Hotels | Blackpool Hotels | Bournemouth Hotels | Bradford Hotels | Brighton Hotels | Bristol Hotels | Cambridge Hotels | Cardiff Hotels | Carlisle Hotels | Chester Hotels | Derby Hotels | Dover Hotels | Dundee Hotels | Durham Hotels | Edinburgh Hotels | Exeter Hotels | Glasgow Hotels | Gloucester Hotels | Inverness Hotels | Ipswich Hotels | Leicester Hotels | Leeds Hotels | Lincoln Hotels | Liverpool Hotels | London Hotels | Manchester Hotels | Middlesbrough Hotels | Newcastle Hotels | Newquay Hotels | Norwich Hotels | Nottingham Hotels | Oxford Hotels | Plymouth Hotels | Reading Hotels | Sheffield Hotels | Southampton Hotels | Stoke on Trent Hotels | Stratford upon Avon Hotels | Swansea Hotels | Telford Hotels | Torquay Hotels</p>
    </section>
  </main>

  <footer class="site-footer">
    <nav><span>Home</span><span>Holiday Park</span><span>Caravan Park</span><span>Hostels</span><span>Hotels</span><span>Travel Lodges</span><span>Camping</span></nav>
    <div class="copyright">© Copyright 2010 Lodging Meadow</div>
  </footer>
</body>
</html>
```